Brochure Design to inject new life into an existing business to scale to North America

I need a brochure for an existing company that is relaunching in the Toronto area called MORvane. We help business professionals improve their professional appearance from head to toe. Our signature product is called R.U.D.A.X. We would like to have the main colours be aqua, blue, charcoal grey, no yellows or orange.

Target Market(s)

business professionals over 40 years old who want to improve their professional appearance in a business casual world , all year long

Font styles to use
Serif
Sans Serif

Colors
0493ce
33a6d7
33b8a4
f8fbef

Requirements
Must have
• Diagrams,
a natural flow
Colour balance
easy to read
aqua, blue, light green and charcoal grey for main colour
Nice to have
• boarders
impact pages
clear and attractive lines
Should not have
• yellow or orange
primary colours
short or sharp angles
black pages

```html
<!DOCTYPE html>
<html lang="en">
<head>
<meta charset="utf-8">
<title>MORvane Style Consultant Brochure</title>
<link href="https://fonts.googleapis.com/css2?family=EB+Garamond:wght@400;500;600&family=Open+Sans:wght@400;600&display=swap" rel="stylesheet">
<style>
:root{
  --teal:#33b8a4;
  --teal-deep:#27a892;
  --blue:#33a6d7;
  --blue-deep:#0493ce;
  --cream:#f8fbef;
  --charcoal:#4a4d52;
  --grey-text:#6b6f75;
  --panel:#eeeff0;
  --paper:#ffffff;
  --backdrop:#e4e5e8;
}
*{margin:0;padding:0;box-sizing:border-box}
html,body{width:1200px;height:3000px;overflow:hidden;background:var(--backdrop)}
body{position:relative;font-family:"EB Garamond",Georgia,serif;color:var(--charcoal)}
.spread{position:absolute;left:60px;width:1080px;height:764px;display:flex;box-shadow:0 6px 22px rgba(0,0,0,.14)}
.spread--cover{top:60px}
.spread--inside{top:1118px}
.spread--method{top:2176px}
.page{position:relative;width:540px;height:764px;background:var(--paper);overflow:hidden}
.page--left{border-right:1px solid #ececec}
.abs{position:absolute}
.brand{font-family:"EB Garamond",Georgia,serif;font-weight:500;color:var(--teal);letter-spacing:.5px;display:flex;align-items:center;gap:8px}
.brand__dot{width:10px;height:10px;border-radius:50%;background:var(--teal)}
.brand__sub{font-family:"Open Sans",Arial,sans-serif;font-size:9px;letter-spacing:1.5px;color:var(--grey-text);text-transform:uppercase}
.photo{position:absolute}
.page-num{position:absolute;bottom:16px;width:18px;height:18px;background:var(--teal);color:#fff;font-family:"Open Sans",Arial,sans-serif;font-size:9px;display:flex;align-items:center;justify-content:center}
.body-copy{font-size:10.5px;line-height:1.45;color:var(--grey-text)}
.body-copy p+p{margin-top:8px}
.band{position:absolute;background:var(--teal)}
.band .body-copy{color:#fff}
/* cover */
.cover-back__brand{left:0;right:0;top:290px;justify-content:center;flex-direction:column;gap:2px}
.cover-back__brand .brand__name{font-size:34px}
.contact{left:0;right:0;top:540px;text-align:center;font-size:10.5px;color:var(--grey-text);line-height:1.5}
.contact__icon{display:block;width:9px;height:9px;margin:8px auto 2px;background:var(--teal);border-radius:2px}
.contact__social{display:flex;gap:5px;justify-content:center;margin-top:6px}
.contact__social span{width:7px;height:7px;border-radius:50%;background:var(--teal)}
.cover-front__brand{right:56px;top:36px;flex-direction:column;align-items:flex-end;gap:0}
.cover-front__brand .brand__name{font-size:28px}
.hero-frame{left:39px;top:100px;width:461px;height:465px;border:9px solid var(--teal)}
.hero-frame .photo{inset:0}
.headline{left:0;right:0;top:590px;text-align:center;color:var(--teal);text-transform:uppercase}
.headline__line1{font-size:21px;letter-spacing:.5px}
.headline__line2{font-size:21px;font-weight:600;letter-spacing:.5px;color:var(--teal-deep)}
.tagline{left:0;right:0;top:660px;text-align:center;font-size:12.5px;color:var(--charcoal)}
.url{left:0;right:0;top:722px;text-align:center;font-size:9px;color:var(--grey-text)}
/* method */
.method-title{left:0;width:540px;top:110px;text-align:center;font-size:58px;letter-spacing:6px;color:var(--grey-text);font-weight:400}
.method-sub{left:0;width:540px;top:196px;text-align:center;font-family:"Open Sans",Arial,sans-serif;font-size:13px;color:var(--grey-text)}
.method-panel{left:0;top:250px;width:540px;height:340px;background:var(--panel)}
.step-card{position:absolute;top:275px;width:88px;height:290px;border-radius:8px;color:#fff;text-align:center;padding-top:16px}
.step-card--teal{background:var(--teal)}
.step-card--blue{background:var(--blue)}
.step-card__letter{font-size:40px;line-height:1}
.step-card__label{font-family:"Open Sans",Arial,sans-serif;font-size:8px;letter-spacing:1px;text-transform:uppercase;margin-top:22px;opacity:.85}
.step-card__text{font-size:10px;line-height:1.3;margin:14px 8px 0}
.step-card svg{position:absolute;left:26px;bottom:20px}
.diagram-title{left:0;right:0;top:116px;text-align:center;font-size:30px;letter-spacing:.5px;color:var(--charcoal)}
.diagram-item{position:absolute;left:86px;width:420px;height:96px;display:flex;align-items:center;gap:30px}
.diagram-item__text h3{font-size:11px;font-weight:600;color:var(--teal);margin-bottom:6px}
.diagram-item__text p{font-size:10.5px;line-height:1.4;color:var(--grey-text)}
</style>
</head>
<body>

<!-- Cover spread -->
<section class="spread spread--cover">
  <div class="page page--left">
    <div class="abs brand cover-back__brand">
      <span class="brand__name">MORvane</span>
      <span class="brand__sub">Style Consultant</span>
    </div>
    <div class="abs contact">
      Mara can make private arrangements to meet<br>with you anywhere in GTA.
      <span class="contact__icon"></span>905.555.0142
      <span class="contact__icon"></span>hello@morvanestyle.com
      <span class="contact__icon"></span>www.morvanestyle.com
      <div class="contact__social"><span></span><span></span><span></span></div>
    </div>
  </div>
  <div class="page page--right">
    <div class="abs brand cover-front__brand">
      <span class="brand__name">MORvane</span>
      <span class="brand__sub">Style Consultant</span>
    </div>
    <div class="abs hero-frame">
      <div class="photo" role="img" aria-label="Businesswoman in a white dress holding a dark clutch on a rooftop above a city" style="background:linear-gradient(160deg,#b9b5ad 0%,#8d8478 40%,#d9d6d1 60%,#6f6358 100%)"></div>
    </div>
    <div class="abs headline">
      <div class="headline__line1">When you get dressed each day,</div>
      <div class="headline__line2">Do you feel confident?</div>
    </div>
    <div class="abs tagline">The Right Image Consultant Can Turn That Chore Into a Joy</div>
    <div class="abs url">www.morvanestyle.com</div>
  </div>
</section>

<!-- Inside spread -->
<section class="spread spread--inside">
  <div class="page page--left">
    <div class="abs body-copy" style="left:37px;top:100px;width:219px">
      <p>We work with men and women over 40 years old who want to improve their professional appearance in a business casual world, all year long.</p>
      <p>At your age through life, building your career, growing a family and hitting milestones, when did you last take time for you? For so many busy professionals, dressing became one more chore. Our service is here to change that, so getting ready feels easy and every outfit supports the person you are today.</p>
    </div>
    <div class="photo" role="img" aria-label="Woman in a grey dress standing with folded arms against a brick wall" style="left:280px;top:60px;width:220px;height:287px;background:linear-gradient(150deg,#9a6a52 0%,#7a5748 45%,#5b5a5e 75%,#8c7466 100%)"></div>
    <div class="band" style="left:0;top:400px;width:540px;height:300px">
      <div class="photo" role="img" aria-label="Pale pink leather handbag beside a person in dark trousers" style="left:37px;top:32px;width:226px;height:232px;background:linear-gradient(135deg,#c9b5b0 0%,#ead6d6 45%,#a86c5c 70%,#3b3335 100%)"></div>
      <div class="abs body-copy" style="left:275px;top:70px;width:225px">
        <p>Have you ever noticed how uncomfortable you feel in ill fitting clothes? We look at the whole picture, from shape and colour to lifestyle, and build a wardrobe that works as hard as you do. Walk into a room and feel sure of yourself, every single day.</p>
      </div>
    </div>
    <div class="page-num" style="left:37px">2</div>
  </div>
  <div class="page page--right">
    <div class="band" style="left:0;top:54px;width:540px;height:305px">
      <div class="abs body-copy" style="left:37px;top:76px;width:219px">
        <p>To stay relevant in the business casual world, it takes more than a new suit. We refine your wardrobe, accessories and grooming so your style feels current, polished and true to you.</p>
      </div>
      <div class="photo" role="img" aria-label="Flat lay of leather belts, watch, sunglasses and a plaid shirt on wood" style="left:274px;top:36px;width:226px;height:232px;background:linear-gradient(135deg,#6b4a35 0%,#9a6b47 40%,#3f5f86 70%,#7a5a40 100%)"></div>
    </div>
    <div class="photo" role="img" aria-label="Rack of blue, teal and neutral garments on hangers" style="left:37px;top:410px;width:225px;height:290px;background:linear-gradient(90deg,#c7bdb2 0%,#3f6f8f 30%,#5fa6b0 55%,#d8d2c8 80%,#9c8f84 100%)"></div>
    <div class="abs body-copy" style="left:288px;top:500px;width:217px">
      <p>One visit helps you stop impulse shopping, pick up quick outfits with ease, and know exactly what suits you. Save time, spend smarter and enjoy the pieces that make you look your best.</p>
    </div>
    <div class="page-num" style="right:37px">3</div>
  </div>
</section>

<!-- Method spread -->
<section class="spread spread--method">
  <div class="page page--left">
    <h1 class="abs method-title">R. U. D. A. X.</h1>
    <div class="abs method-sub">Steps in methodology</div>
    <div class="abs method-panel"></div>

    <div class="step-card step-card--teal" style="left:32px">
      <div class="step-card__letter">R</div>
      <div class="step-card__label">Refine</div>
      <div class="step-card__text">Elevate your daily presence</div>
      <svg width="36" height="30" viewBox="0 0 36 30" fill="none" stroke="#fff" stroke-width="1.8" stroke-linejoin="round"><path d="M4 24 L6 8 L13 15 L18 5 L23 15 L30 8 L32 24 Z"/></svg>
    </div>
    <div class="step-card step-card--blue" style="left:130px">
      <div class="step-card__letter">U</div>
      <div class="step-card__label">Upgrade</div>
      <div class="step-card__text">How it shapes your image</div>
      <svg width="36" height="30" viewBox="0 0 36 30" fill="none" stroke="#fff" stroke-width="1.8"><circle cx="18" cy="15" r="12"/><circle cx="18" cy="15" r="6"/><circle cx="18" cy="15" r="1.5" fill="#fff"/></svg>
    </div>
    <div class="step-card step-card--teal" style="left:228px">
      <div class="step-card__letter">D</div>
      <div class="step-card__label">Define</div>
      <div class="step-card__text">Your energy and tone</div>
      <svg width="36" height="30" viewBox="0 0 36 30" fill="none" stroke="#fff" stroke-width="1.8" stroke-linecap="round"><circle cx="18" cy="15" r="3" fill="#fff"/><path d="M11 8 A10 10 0 0 0 11 22 M25 8 A10 10 0 0 1 25 22 M6 4 A16 16 0 0 0 6 26 M30 4 A16 16 0 0 1 30 26"/></svg>
    </div>
    <div class="step-card step-card--blue" style="left:326px">
      <div class="step-card__letter">A</div>
      <div class="step-card__label">Align</div>
      <div class="step-card__text">Empowerment</div>
      <svg width="36" height="30" viewBox="0 0 36 30" fill="none" stroke="#fff" stroke-width="1.8" stroke-linejoin="round"><circle cx="18" cy="12" r="9"/><path d="M12 19 L9 29 L14 26 L16 29 M24 19 L27 29 L22 26 L20 29"/></svg>
    </div>
    <div class="step-card step-card--teal" style="left:424px">
      <div class="step-card__letter">X</div>
      <div class="step-card__label">Excel</div>
      <div class="step-card__text">Save time, spend less</div>
      <svg width="36" height="30" viewBox="0 0 36 30" fill="none" stroke="#fff" stroke-width="1.8" stroke-linecap="round"><circle cx="18" cy="15" r="12"/><path d="M18 8 V15 L23 18"/></svg>
    </div>
    <div class="page-num" style="left:37px">4</div>
  </div>

  <div class="page page--right">
    <h2 class="abs diagram-title">PROBABLY A DIAGRAM</h2>

    <div class="diagram-item" style="top:196px">
      <svg width="96" height="96" viewBox="0 0 96 96"><path d="M48 6 A42 42 0 1 1 14 72" fill="none" stroke="var(--teal)" stroke-width="5" stroke-linecap="round"/><circle cx="48" cy="48" r="32" fill="var(--blue)"/><path d="M36 49 L45 58 L61 40" fill="none" stroke="#fff" stroke-width="4" stroke-linecap="round" stroke-linejoin="round"/></svg>
      <div class="diagram-item__text"><h3>Individual style</h3><p>Improve your self esteem. Increase your confidence.<br>Feel really happy with your appearance.</p></div>
    </div>
    <div class="diagram-item" style="top:294px">
      <svg width="96" height="96" viewBox="0 0 96 96"><path d="M48 6 A42 42 0 1 1 14 72" fill="none" stroke="var(--teal)" stroke-width="5" stroke-linecap="round"/><circle cx="48" cy="48" r="32" fill="var(--blue)"/><path d="M48 32 L52 44 L64 44 L54 51 L58 63 L48 56 L38 63 L42 51 L32 44 L44 44 Z" fill="#fff"/></svg>
      <div class="diagram-item__text"><h3>Next level business attire</h3><p>Be seen, taken seriously. Understand strength.<br>Get noticed at work.</p></div>
    </div>
    <div class="diagram-item" style="top:392px">
      <svg width="96" height="96" viewBox="0 0 96 96"><path d="M48 6 A42 42 0 1 1 14 72" fill="none" stroke="var(--teal)" stroke-width="5" stroke-linecap="round"/><circle cx="48" cy="48" r="32" fill="var(--blue)"/><circle cx="48" cy="40" r="6" fill="#fff"/><circle cx="35" cy="52" r="6" fill="#fff"/><circle cx="61" cy="52" r="6" fill="#fff"/></svg>
      <div class="diagram-item__text"><h3>Positive message in leadership</h3><p>Increase your confidence in your wardrobe.<br>Always make a great impression.</p></div>
    </div>
    <div class="diagram-item" style="top:490px">
      <svg width="96" height="96" viewBox="0 0 96 96"><path d="M48 6 A42 42 0 1 1 14 72" fill="none" stroke="var(--teal)" stroke-width="5" stroke-linecap="round"/><circle cx="48" cy="48" r="32" fill="var(--blue)"/><path d="M34 48 H62 M52 38 L62 48 L52 58" fill="none" stroke="#fff" stroke-width="4" stroke-linecap="round" stroke-linejoin="round"/></svg>
      <div class="diagram-item__text"><h3>Business Casual vs Business Professional</h3><p>Business professional vs business casual.<br>Learn when and how to use it.<br>How to identify the differences.</p></div>
    </div>
    <div class="diagram-item" style="top:592px">
      <svg width="96" height="96" viewBox="0 0 96 96"><path d="M48 6 A42 42 0 1 1 14 72" fill="none" stroke="var(--teal)" stroke-width="5" stroke-linecap="round"/><circle cx="48" cy="48" r="32" fill="var(--blue-deep)"/><circle cx="48" cy="48" r="16" fill="none" stroke="#fff" stroke-width="3"/><path d="M48 39 V48 L54 52" fill="none" stroke="#fff" stroke-width="3" stroke-linecap="round"/></svg>
      <div class="diagram-item__text"><h3>5 minute mornings</h3><p>Feel good about the way you look and feel.<br>Save valuable time and money. Update your routines.</p></div>
    </div>
    <div class="page-num" style="right:37px">5</div>
  </div>
</section>

</body>
</html>
```